Criação de Papelaria Profissional para Consultoria de Negócios
A empresa queria:
" Serviços de Consultoria de Carreira (transição, desenvolvimento de liderança), Assessment, Coaching, Outplacement, Headhunting "

```html
<!DOCTYPE html>
<html lang="pt-BR">
<head>
<meta charset="UTF-8">
<title>Lívia Moretti – Cartões de Visita</title>
<link rel="stylesheet" href="https://fonts.googleapis.com/css2?family=Josefin+Sans:wght@300;400&display=swap">
<style>
  :root {
    --page-bg: #ecebe8;
    --burgundy: #6e1420;
    --burgundy-deep: #3f0a12;
    --burgundy-light: #8a2230;
    --paper: #ffffff;
    --ink: #4a4a4a;
    --ink-soft: #7a7a7a;
    --silver-1: #f4f4f4;
    --silver-2: #a9a9ab;
    --watermark: #ededed;
  }
  * { box-sizing: border-box; margin: 0; padding: 0; }
  html, body { width: 1200px; height: 1200px; overflow: hidden; }
  body {
    background: var(--page-bg);
    font-family: "Josefin Sans", sans-serif;
    display: flex;
    align-items: center;
    justify-content: center;
    gap: 60px;
  }
  .card {
    position: relative;
    width: 530px;
    height: 303px;
    overflow: hidden;
    box-shadow: 0 6px 18px rgba(0,0,0,0.14);
  }

  /* Front */
  .card--front {
    background: radial-gradient(ellipse at 50% 40%, var(--burgundy-light) 0%, var(--burgundy) 45%, var(--burgundy-deep) 100%);
    color: var(--paper);
    display: flex;
    flex-direction: column;
    align-items: center;
    justify-content: center;
  }
  .front-mark {
    width: 54px;
    height: 54px;
    border: 1.5px solid var(--paper);
    border-radius: 50%;
    margin-bottom: 18px;
  }
  .front-name {
    font-weight: 300;
    font-size: 34px;
    letter-spacing: 2px;
    text-transform: uppercase;
    line-height: 1;
  }
  .front-role {
    margin-top: 10px;
    font-size: 11px;
    letter-spacing: 4px;
    text-transform: uppercase;
    opacity: 0.85;
  }
  .silver-tab {
    position: absolute;
    right: 0;
    top: 118px;
    width: 58px;
    height: 60px;
    border-radius: 6px 0 0 6px;
    background: linear-gradient(180deg, var(--silver-1), var(--silver-2) 55%, var(--silver-1));
  }

  /* Back */
  .card--back { background: var(--paper); color: var(--ink); }
  .back-watermark {
    position: absolute;
    left: 150px;
    top: 40px;
    width: 230px;
    height: 230px;
    border: 22px solid var(--watermark);
    border-radius: 50%;
  }
  .back-mark {
    position: absolute;
    right: 60px;
    top: 56px;
    width: 110px;
    height: 110px;
    border: 3px solid var(--burgundy);
    border-radius: 50%;
  }
  .back-identity {
    position: absolute;
    left: 34px;
    top: 40px;
  }
  .back-name {
    font-weight: 300;
    font-size: 27px;
    letter-spacing: 1.5px;
    text-transform: uppercase;
    line-height: 1;
  }
  .back-role {
    margin-top: 7px;
    font-size: 8.5px;
    letter-spacing: 3px;
    text-transform: uppercase;
    color: var(--ink-soft);
  }
  .contact-list {
    position: absolute;
    left: 34px;
    top: 132px;
    list-style: none;
    display: flex;
    flex-direction: column;
    gap: 12px;
  }
  .contact-item {
    display: flex;
    align-items: center;
    gap: 10px;
    font-size: 11px;
    line-height: 1.35;
    color: var(--ink);
  }
  .contact-icon {
    width: 16px;
    height: 16px;
    flex: none;
  }
</style>
</head>
<body>

  <section class="card card--front">
    <div class="front-mark"></div>
    <h1 class="front-name">Lívia Moretti</h1>
    <p class="front-role">Consultoria de Carreira</p>
    <div class="silver-tab"></div>
  </section>

  <section class="card card--back">
    <div class="back-watermark"></div>
    <div class="back-mark"></div>

    <div class="back-identity">
      <h2 class="back-name">Lívia Moretti</h2>
      <p class="back-role">Consultoria de Carreira</p>
    </div>

    <ul class="contact-list">
      <li class="contact-item">
        <svg class="contact-icon" viewBox="0 0 16 16" aria-hidden="true">
          <circle cx="8" cy="8" r="8" fill="var(--burgundy)"/>
          <path d="M5.2 4.2l1.4 0 .6 1.8-.9.7c.5 1 1.2 1.7 2.2 2.2l.7-.9 1.8.6 0 1.4c-3.4.2-6-2.4-5.8-5.8z" fill="#fff"/>
        </svg>
        <span>(11) 4002-0000<br>(11) 98000-0000</span>
      </li>
      <li class="contact-item">
        <svg class="contact-icon" viewBox="0 0 16 16" aria-hidden="true">
          <circle cx="8" cy="8" r="8" fill="var(--burgundy)"/>
          <rect x="4" y="5" width="8" height="6" fill="none" stroke="#fff" stroke-width="1"/>
          <path d="M4 5l4 3.2L12 5" fill="none" stroke="#fff" stroke-width="1"/>
        </svg>
        <span>contato@liviamoretti.com.br<br>www.liviamoretti.com.br</span>
      </li>
      <li class="contact-item">
        <svg class="contact-icon" viewBox="0 0 16 16" aria-hidden="true">
          <circle cx="8" cy="8" r="8" fill="var(--burgundy)"/>
          <path d="M8 3.6a2.7 2.7 0 0 0-2.7 2.7C5.3 8.4 8 12 8 12s2.7-3.6 2.7-5.7A2.7 2.7 0 0 0 8 3.6z" fill="#fff"/>
          <circle cx="8" cy="6.3" r="1" fill="var(--burgundy)"/>
        </svg>
        <span>Rua das Palmeiras, 120 - Sala 4<br>São Paulo - SP · 01000-000</span>
      </li>
    </ul>
  </section>

</body>
</html>
```